Lotus Bowl take out menu

We need a take out menu design using our menu attached. Info to include would be our address: 5817 Meridel Harrow Pkwy #204, Lafayette, LA 70508. Phone number is 337-614-2953. website is www.lotusbowlvtr.example.

Industry/Entity Type

Asian Restaurant

```html
<!DOCTYPE html>
<html lang="en">
<head>
<meta charset="utf-8">
<title>Lotus Bowl – Take Out Menu</title>
<link rel="stylesheet" href="https://fonts.googleapis.com/css2?family=Aladin&family=Kalam:wght@300;400;700&display=swap">
<style>
  :root{
    --red:#a3242a;
    --ink:#2b1f20;
    --paper:#f4eaeb;
    --paper-deep:#ecdcde;
    --rule:#c9bcbd;
    --divider:#b9a9aa;
  }
  *{margin:0;padding:0;box-sizing:border-box}
  html,body{width:1200px;height:853px;overflow:hidden;background:var(--paper)}
  body{position:relative;font-family:"Kalam",cursive;color:var(--ink)}
  h2,h3{font-weight:400}
  .backdrop{position:absolute;inset:0;background:
      radial-gradient(ellipse at 30% 40%, #f7eff0 0%, transparent 60%),
      radial-gradient(ellipse at 80% 70%, #f6eced 0%, transparent 55%),
      linear-gradient(180deg,var(--paper) 0%,var(--paper-deep) 100%)}
  .top-rule{position:absolute;top:30px;height:1.5px;background:var(--red)}
  .v-divider{position:absolute;top:40px;width:1px;height:782px;background:var(--divider)}

  .brand{position:absolute;left:440px;top:34px;width:320px;text-align:center}
  .brand-name{display:flex;align-items:center;justify-content:center;gap:8px;font-family:"Kalam",cursive;font-weight:700;font-size:30px;line-height:34px;color:#111}
  .brand-dot{width:22px;height:22px;border-radius:50%;background:var(--red)}
  .brand-tag{font-family:"Kalam",cursive;font-weight:700;font-size:9px;letter-spacing:1.8px;margin-top:-4px;color:#111}
  .brand-contact{font-size:7.6px;line-height:9px;font-weight:400;color:var(--ink);margin-top:1px}

  .col{position:absolute}
  .section{position:absolute;left:0;right:0}
  .heading{font-family:"Aladin",cursive;color:var(--red);font-size:17px;letter-spacing:1.5px;text-align:center;line-height:20px}
  .subheading{font-family:"Aladin",cursive;color:var(--ink);font-size:11px;letter-spacing:1.2px;text-align:center;line-height:14px}

  .item{display:flex;justify-content:space-between;align-items:flex-start;border-bottom:1px solid var(--rule);padding:3px 0 4px}
  .item:last-child{border-bottom:none}
  .loose .item{padding:6px 0 5px}
  .snug .item{padding:2px 0 3px}
  .name{color:var(--red);font-size:9px;line-height:10px;font-weight:400;display:flex;align-items:center;gap:2px;white-space:nowrap}
  .desc{font-size:8.2px;line-height:10px;font-weight:300;white-space:nowrap}
  .price{font-size:9px;line-height:10px;font-weight:400;padding-top:2px;white-space:nowrap}
  .chili{width:11px;height:8px;fill:var(--red)}

  .drink-head{position:absolute;color:var(--red);font-size:8.6px;line-height:11px}
  .drink-list{position:absolute;font-size:8.2px;line-height:10.75px;font-weight:300;white-space:nowrap}
  .drink-price{position:absolute;font-size:8.2px;line-height:10.75px;font-weight:300;text-align:right}
  .beer-sep{position:absolute;width:1px;background:var(--rule)}
</style>
</head>
<body>
<svg width="0" height="0" style="position:absolute" aria-hidden="true">
  <defs>
    <symbol id="chili" viewBox="0 0 22 16">
      <path d="M2 13c5 2 13-1 16-8 1-2 0-3-1-3-2 0-3 2-4 3-3 4-7 6-11 6-1 0-1 2 0 2z"/>
      <path d="M16 2c1-1 3-2 5-1" stroke="#a3242a" stroke-width="1.4" fill="none"/>
    </symbol>
  </defs>
</svg>

<div class="backdrop" role="img" aria-label="Faint line pattern of swirling waves and dragons in pale pink tones"></div>

<div class="top-rule" style="left:0;width:473px"></div>
<div class="top-rule" style="left:746px;width:454px"></div>
<div class="v-divider" style="left:402px"></div>
<div class="v-divider" style="left:797px"></div>

<header class="brand">
  <div class="brand-name"><span class="brand-dot"></span>Lotus Bowl</div>
  <div class="brand-tag">FRESH ASIAN CUISINE</div>
  <div class="brand-contact">5817 Meridel Harrow Pkwy #204, Lafayette, LA 70508<br>337-614-2953 · www.lotusbowlvtr.example</div>
</header>

<!-- Left column -->
<main class="col" style="left:28px;top:0;width:357px;height:853px">
  <section class="section loose" style="top:40px">
    <h2 class="heading">ENTREES</h2>
    <h3 class="subheading" style="margin:4px 0 6px">CHEF SPECIALTIES</h3>
    <div class="item"><div><div class="name">Jasmine Tea Smoked Duck</div><div class="desc">Boneless half duck served with thinly sliced cucumber, scallion, house made duck<br>sauce and soft flour wrap</div></div><div class="price">$24</div></div>
    <div class="item"><div><div class="name">Sizzling Cumin' Lamb <svg class="chili"><use href="#chili"/></svg></div><div class="desc">Tender pieces of lamb rubbed in cumin, Sichuan peppers, celery and cilantro</div></div><div class="price">$16</div></div>
    <div class="item"><div><div class="name">Chef Lin's Spicy Beef <svg class="chili"><use href="#chili"/></svg><svg class="chili"><use href="#chili"/></svg></div><div class="desc">Angus beef in house made green peppercorn sauce, drizzled with fresh Sichuan<br>peppercorn, Thai chili and cilantro</div></div><div class="price">$16</div></div>
    <div class="item"><div><div class="name">Chef Lin's Spicy Fish <svg class="chili"><use href="#chili"/></svg><svg class="chili"><use href="#chili"/></svg></div><div class="desc">Fish filet in house made green peppercorn sauce, drizzled with fresh Sichuan<br>peppercorn, Thai chili and cilantro</div></div><div class="price">$17</div></div>
    <div class="item"><div><div class="name">General Tso's Scallops <svg class="chili"><use href="#chili"/></svg></div><div class="desc">The perfect combination of tender scallops marinated in a sweet chili sauce<br>with broccoli and red peppers</div></div><div class="price">$18</div></div>
  </section>

  <section class="section" style="top:297px">
    <h3 class="subheading" style="margin-bottom:10px">BEEF &amp; PORK</h3>
    <div class="item"><div><div class="name">Dancing Beef <svg class="chili"><use href="#chili"/></svg><svg class="chili"><use href="#chili"/></svg><svg class="chili"><use href="#chili"/></svg></div><div class="desc">Angus Beef slices on a bed of sizzling rice crackers, black peppercorn and<br>Thai chili</div></div><div class="price">$16</div></div>
    <div class="item"><div><div class="name">Oyster Beef</div><div class="desc">Tender cuts of steak wok fried and marinated in a homemade oyster sauce</div></div><div class="price">$14</div></div>
    <div class="item"><div><div class="name">Double Pepper Beef <svg class="chili"><use href="#chili"/></svg><svg class="chili"><use href="#chili"/></svg><svg class="chili"><use href="#chili"/></svg></div><div class="desc">Angus Steak cubes with fresh green peppercorn, Thai chili, Serrano Pepper and<br>celery</div></div><div class="price">$16</div></div>
    <div class="item"><div><div class="name">Black Pepper Steak <svg class="chili"><use href="#chili"/></svg></div><div class="desc">Tender cuts of steak mixed with onions and red and green bell peppers</div></div><div class="price">$15</div></div>
    <div class="item"><div><div class="name">Singapore Baby Back Ribs</div><div class="desc">Tender Baby back ribs rubbed in a Thai inspired sweet tangy glaze</div></div><div class="price">$16</div></div>
    <div class="item"><div><div class="name">Dancing Pork Belly</div><div class="desc">Braised Pork Belly on sizzling rice cracker</div></div><div class="price">$15</div></div>
    <div class="item"><div><div class="name">Twice Cooked Pork <svg class="chili"><use href="#chili"/></svg></div><div class="desc">Stir fried Pork Belly slices with leek and fermented black beans</div></div><div class="price">$14</div></div>
  </section>

  <section class="section" style="top:548px">
    <h3 class="subheading" style="margin-bottom:12px">CHICKEN</h3>
    <div class="item"><div><div class="name">Kung Pao Chicken <svg class="chili"><use href="#chili"/></svg></div><div class="desc">Chicken sautéed with roasted peanuts and scallions, dry red chili and whole<br>Sichuan peppercorns in Kung Pao sauce</div></div><div class="price">$13</div></div>
    <div class="item"><div><div class="name">Orange Chicken</div><div class="desc">Battered-fried chicken breast with dried chili peppers and stir fried in a tangy<br>orange flavored sauce</div></div><div class="price">$13</div></div>
    <div class="item"><div><div class="name">Double Pepper Chicken <svg class="chili"><use href="#chili"/></svg><svg class="chili"><use href="#chili"/></svg><svg class="chili"><use href="#chili"/></svg></div><div class="desc">Farm raised chicken cube with fresh green peppercorn, Thai chili, Serrano<br>peppers, and jalapenos</div></div><div class="price">$15</div></div>
    <div class="item"><div><div class="name">Crispy Spicy Chicken <svg class="chili"><use href="#chili"/></svg><svg class="chili"><use href="#chili"/></svg></div><div class="desc">Crispy diced chicken with Sichuan peppers, cilantro and sesame</div></div><div class="price">$14</div></div>
    <div class="item"><div><div class="name">General Tso's Chicken <svg class="chili"><use href="#chili"/></svg></div><div class="desc">Battered-fried chicken breast, stir-fried in a sweet &amp; tangy chili sauce, scallions<br>and chili pepper</div></div><div class="price">$13</div></div>
    <div class="item"><div><div class="name">Shredded Chicken in Spicy Garlic Sauce <svg class="chili"><use href="#chili"/></svg></div><div class="desc">Tender shredded chicken, wood ear fungus, bamboo shoots in a classic spicy<br>garlic sauce</div></div><div class="price">$14</div></div>
    <div class="item"><div><div class="name">Sweet &amp; Sour Chicken</div><div class="desc">Crispy Chicken glazed in a homemade sweet &amp; sour marinade</div></div><div class="price">$13</div></div>
  </section>
</main>

<!-- Middle column -->
<div class="col" style="left:420px;top:0;width:356px;height:853px">
  <section class="section loose" style="top:98px">
    <h2 class="heading">ENTREES</h2>
    <h3 class="subheading" style="margin:3px 0 6px">SEAFOOD</h3>
    <div class="item"><div><div class="name">Kung Pao Shrimp <svg class="chili"><use href="#chili"/></svg></div><div class="desc">Sautéed shrimp with roasted peanuts and scallions, dry red chili and whole<br>Sichuan peppercorns in Kung Pao sauce</div></div><div class="price">$16</div></div>
    <div class="item"><div><div class="name">Rice Wine Shrimp &amp; Tofu <svg class="chili"><use href="#chili"/></svg></div><div class="desc">Shrimp and Tofu braised in garlic pickled pepper sauce with rice wine</div></div><div class="price">$18</div></div>
    <div class="item"><div><div class="name">Shrimp in Spicy Garlic Sauce <svg class="chili"><use href="#chili"/></svg></div><div class="desc">Shrimp sautéed with jicama ginger, garlic and scallions in a spicy garlic sauce</div></div><div class="price">$15</div></div>
    <div class="item"><div><div class="name">Lemon Peel Shrimp</div><div class="desc">Shrimp with fresh lemons in a sweet lemon sauce with vegetables</div></div><div class="price">$15</div></div>
    <div class="item"><div><div class="name">Rice Wine Fish <svg class="chili"><use href="#chili"/></svg></div><div class="desc">White fish filet braised in pickled pepper sauce with rice wine</div></div><div class="price">$14</div></div>
  </section>

  <section class="section" style="top:320px">
    <h2 class="heading" style="margin-bottom:12px">NOODLES &amp; RICE</h2>
    <div class="item"><div><div class="name">Lotus Bowl Fried Rice</div><div class="desc">Shrimp, chicken, and beef, farm fresh eggs, onions, and scallions</div></div><div class="price">$12</div></div>
    <div class="item"><div><div class="name">Vegetarian White Fried Rice</div><div class="desc">Mixed vegetables with white rice</div></div><div class="price">$10</div></div>
    <div class="item"><div><div class="name">Lotus Bowl Lo Mein</div><div class="desc">Shrimp, chicken, and beef, farm fresh eggs, onions, and scallions</div></div><div class="price">$12</div></div>
    <div class="item"><div><div class="name">Vegetarian Lo Mein</div><div class="desc">Mixed vegetables with lo mein noodles</div></div><div class="price">$10</div></div>
  </section>

  <section class="section snug" style="top:474px">
    <h2 class="heading" style="margin-bottom:16px">VEGETARIAN DISHES</h2>
    <div class="item"><div><div class="name">Wok Tossed String Beans <svg class="chili"><use href="#chili"/></svg></div><div class="desc">Fresh string beans mixed with pickled vegetables</div></div><div class="price">$9</div></div>
    <div class="item"><div><div class="name">Mapo Tofu <svg class="chili"><use href="#chili"/></svg><svg class="chili"><use href="#chili"/></svg></div><div class="desc">Soft Tofu, scallion, Sichuan peppercorn and peppers</div></div><div class="price">$11</div></div>
    <div class="item"><div><div class="name">Spicy Garlic Eggplant <svg class="chili"><use href="#chili"/></svg></div><div class="desc">Chinese eggplant in spicy garlic sauce drizzled with scallions</div></div><div class="price">$12</div></div>
    <div class="item"><div><div class="name">Buddha's Delight</div><div class="desc">Seasonal vegetables wok-tossed in our light soy garlic sauce</div></div><div class="price">$10</div></div>
    <div class="item"><div><div class="name">Stir-fried Eggplant Beans <svg class="chili"><use href="#chili"/></svg></div><div class="desc">Chinese eggplant with sautéed green beans</div></div><div class="price">$12</div></div>
    <div class="item"><div><div class="name">Shiitake Baby Bok-Choy</div><div class="desc">Sautéed baby bok-choy with Shiitake mushrooms in brown sauce</div></div><div class="price">$12</div></div>
  </section>

  <section class="section" style="top:682px">
    <h2 class="heading" style="margin-bottom:14px">KIDS MENU</h2>
    <div class="item"><div><div class="name">Beef Lo Mein</div><div class="desc">Lo Mein noodles mixed with beef in garlic sauce</div></div><div class="price">$5</div></div>
    <div class="item"><div><div class="name">Chicken Fried Rice</div><div class="desc">Fried rice, farm fresh eggs, onions, and scallions</div></div><div class="price">$5</div></div>
    <div class="item"><div><div class="name">Sweet &amp; Sour Chicken</div><div class="desc">Bite sized crispy chicken with sweet &amp; sour sauce</div></div><div class="price">$6</div></div>
    <div class="item"><div><div class="name">Lemon Chicken</div><div class="desc">Bite sized crispy chicken in a sweet lemon sauce</div></div><div class="price">$6</div></div>
  </section>
</div>

<!-- Right column -->
<div class="col" style="left:810px;top:0;width:360px;height:853px">
  <section class="section" style="top:42px">
    <h2 class="heading" style="margin-bottom:6px">DESSERTS</h2>
    <div class="item"><div><div class="name">The Great Wall of Cake</div><div class="desc">Scale this fortress of Chocolate Cake Delight</div></div><div class="price">$7</div></div>
    <div class="item"><div><div class="name">Cheesecake Wontons (4)</div><div class="desc">Fried wontons stuffed with cheesecake and dipped in raspberry sauce</div></div><div class="price">$6</div></div>
    <div class="item"><div><div class="name">Tempura Snowball</div><div class="desc">Vanilla ice cream fried in tempura batter with powdered sugar and fudge</div></div><div class="price">$4</div></div>
    <div class="item"><div><div class="name">Sweet Rice Patties in Caramel</div><div class="desc">Traditional Chinese dessert with sweet rice dipped in a caramel sauce</div></div><div class="price">$7</div></div>
  </section>

  <section class="section" style="top:181px;height:340px">
    <h2 class="heading">BUDDHA'S BAR MENU</h2>
    <h3 class="subheading" style="margin-top:6px">BEER</h3>

    <div class="drink-head" style="left:0;top:44px">Domestic</div><div class="drink-price" style="left:50px;width:22px;top:44px">$3</div>
    <div class="drink-list" style="left:0;top:58px">Brook Light<br>Bramwell<br>Corrin Light<br>Michan Ultra<br>Millford Lite<br>Yarrowling</div>
    <div class="beer-sep" style="left:84px;top:44px;height:80px"></div>
    <div class="drink-head" style="left:92px;top:44px">Domestic</div><div class="drink-price" style="left:142px;width:22px;top:44px">$4</div>
    <div class="drink-list" style="left:92px;top:58px">Abren Amber<br>Canefield<br>Envara<br>Blue Harbor</div>
    <div class="beer-sep" style="left:176px;top:44px;height:80px"></div>
    <div class="drink-head" style="left:184px;top:44px">Imports</div><div class="drink-price" style="left:233px;width:22px;top:44px">$4</div>
    <div class="drink-list" style="left:184px;top:58px">Coralla<br>Heidvik<br>Stelvia Arto<br>Sanrei Premium<br>Sinara<br>Kiran Ichi</div>
    <div class="beer-sep" style="left:267px;top:44px;height:80px"></div>
    <div class="drink-head" style="left:276px;top:44px">N/A Beer</div><div class="drink-price" style="left:327px;width:22px;top:44px">$3</div>
    <div class="drink-list" style="left:276px;top:58px">Odwells</div>

    <h3 class="subheading" style="position:absolute;left:0;right:0;top:139px">WINES</h3>

    <div class="drink-head" style="left:0;top:163px">White</div>
    <div class="drink-list" style="left:0;top:177px">Jory Chardonnay<br>Smokeline Chardonnay<br>Aranella Pinot Grigio<br>K Vineyard Pinot Gris<br>Stirling Vale Sauv. Blanc<br>Whitecove Sauvignon Blanc<br>Wendel River Bank Riesling<br>Mia Dolente Moscato</div>
    <div class="drink-price" style="left:104px;width:20px;top:177px">$7<br>$8<br>$6<br>$8<br>$7<br>$9<br>$6<br>$7</div>

    <div class="drink-head" style="left:137px;top:163px">Reds</div>
    <div class="drink-list" style="left:137px;top:177px">Jory Cabernet<br>Alder Valley Cabernet<br>Ghost Hollow Merlot<br>Chateau St Lune Pinot Noir<br>Oyster Cove Pinot Noir<br>21 Verdicts Red Blend<br>Bellinger White Zinfandel</div>
    <div class="drink-price" style="left:241px;width:20px;top:177px">$7<br>$9<br>$9<br>$7<br>$8<br>$7<br>$5</div>

    <div class="drink-head" style="left:276px;top:163px">Sparkling</div>
    <div class="drink-list" style="left:276px;top:177px">Fresanet Brut<br>Zolan Prosecco<br>Chardeau Brut</div>
    <div class="drink-price" style="left:340px;width:20px;top:177px">$6<br>$6<br>$45</div>

    <div class="drink-head" style="left:0;top:270px">Sake</div>
    <div class="drink-list" style="left:0;top:285px">Getsurin (Hot)<br>Jade&amp;Gold (Hot)<br>Pear (Cold)<br>Plum (Cold)<br>Lychee (Cold)</div>
    <div class="drink-price" style="left:104px;width:20px;top:285px">$5<br>$10<br>$8<br>$8<br>$8</div>

    <div class="drink-head" style="left:137px;top:270px">House Wine</div>
    <div class="drink-list" style="left:137px;top:285px">Chardonnay<br>Cabernet<br>Merlot</div>
    <div class="drink-price" style="left:241px;width:20px;top:285px">$6<br>$6<br>$6</div>
  </section>

  <section class="section snug" style="top:525px">
    <h3 class="subheading" style="margin-bottom:3px">SPECIALITY COCKTAILS</h3>
    <div class="item"><div><div class="name">Sake-Tini Drop</div><div class="desc">J.R. Marlow Rice Vodka mixed with Asian pear sake, simple syrup and sour mix</div></div><div class="price">$9</div></div>
    <div class="item"><div><div class="name">Raz/Pom Martini</div><div class="desc">Raspberry Vodka with a pomegranate liqueur and sour mix</div></div><div class="price">$8</div></div>
    <div class="item"><div><div class="name">Lemon Ginger Drop Martini</div><div class="desc">Kestrel 1 Citron, Bellvista ginger zest and sour mix</div></div><div class="price">$8</div></div>
    <div class="item"><div><div class="name">Lotus Blossom</div><div class="desc">Pear Vodka, sparkling sake with Lychee nuts and simple syrup</div></div><div class="price">$9</div></div>
    <div class="item"><div><div class="name">Beijing Fashioned</div><div class="desc">Barrow Rye and Plum bitters with simple syrup and orange &amp; black cherries</div></div><div class="price">$9</div></div>
    <div class="item"><div><div class="name">Samurai Smash</div><div class="desc">Barrow Bourbon mixed with black cherry puree, sour mix and a touch of lemon</div></div><div class="price">$9</div></div>
    <div class="item"><div><div class="name">Cosmic Mandarin</div><div class="desc">Kestrel 1 Orange with Cortelle, cranberry juice and sour mix</div></div><div class="price">$6</div></div>
    <div class="item"><div><div class="name">Lotus Bloody Mary</div><div class="desc">A specially blended Asian infused Vodka with a spicy Bloody Mary mix</div></div><div class="price">$6</div></div>
    <div class="item"><div><div class="name">Cucumber Smash</div><div class="desc">Novet Gin, simple syrup, sour mix with cucumber slices and fresh mint</div></div><div class="price">$9</div></div>
    <div class="item"><div><div class="name">Sake Mojito</div><div class="desc">Captain Merrick White Rum mixed with sake a splash of lime juice and fresh mint</div></div><div class="price">$9</div></div>
    <div class="item"><div><div class="name">Top Shelf Margarita</div><div class="desc">Don Aurelio Silver with Cortelle, rita mix and Grand Mareil float</div></div><div class="price">$10</div></div>
  </section>
</div>
</body>
</html>
```